Kettles - Eggs For Sale Sign

Would like a graphic quality image of a EGGS FOR SALE SIGN ... am getting a local outdoor sign company to print the sign and attach it to a frame.

this is going to be outside by the gate to our farm ... would like the sign to "POP" ... DRAW ATTENTION ... as it were ... please.

I think we need it about 36”(w) x 30”(h) ... maybe 48”x36” ... not sure ... need about an extra 1 1/2” border around also so that we can frame this into a wooden frame ...

The color picture is similar to the pattern we like ... the fonts you are welcome to just blow us out of the water with ... we are not tied down to any particular font ... like the “WANTED” posters of old ... sorta.

Logo Text

Bramble Nook Acres

Colors

Requirements
Must have
• Some type of Fire Fly art ... not to modern ... not too comic book ...
Nice to have
• phone number
• call or text

```html
<!DOCTYPE html>
<html lang="en">
<head>
<meta charset="utf-8">
<title>Bramble Nook Acres – Eggs For Sale Sign</title>
<link href="https://fonts.googleapis.com/css2?family=Kaushan+Script&family=Anton&family=Libre+Baskerville:wght@700&display=swap" rel="stylesheet">
<style>
  :root {
    --board-bg: #bcbcbc;
    --sheet-bg: #ffffff;
    --wood-dark: #2e170c;
    --wood-mid: #55301c;
    --wood-light: #74452a;
    --teal: #5ea7b2;
    --teal-light: #bfe6ef;
    --teal-rim: #e2cfc6;
    --glow: #f2a23a;
    --ink: #111111;
    --white: #ffffff;
    --bar-edge: #3fb3c4;
  }
  * { margin: 0; padding: 0; box-sizing: border-box; }
  html, body { width: 960px; height: 1200px; overflow: hidden; }
  body { position: relative; background: var(--sheet-bg); }

  .presentation-board {
    position: absolute; left: 0; top: 0; width: 960px; height: 832px;
    background: var(--board-bg);
  }
  .sign-shadow {
    position: absolute; left: 120px; top: 672px; width: 720px; height: 34px;
    border-radius: 50%;
    background: radial-gradient(ellipse at center, rgba(0,0,0,.5), rgba(0,0,0,0) 70%);
  }
  .sign {
    position: absolute; left: 78px; top: 82px; width: 804px; height: 602px;
    overflow: hidden;
  }
  .sign-wood {
    position: absolute; inset: 0;
    background:
      repeating-linear-gradient(90deg, rgba(0,0,0,.45) 0 2px, transparent 2px 62px),
      repeating-linear-gradient(90deg, rgba(255,255,255,.04) 0 20px, rgba(0,0,0,.08) 20px 44px, transparent 44px 62px),
      linear-gradient(90deg, var(--wood-dark), var(--wood-mid) 22%, var(--wood-light) 50%, var(--wood-mid) 78%, var(--wood-dark));
  }
  .corner-ornament {
    position: absolute; width: 144px; height: 136px;
    background: radial-gradient(ellipse at center, rgba(255,255,255,.16), rgba(255,255,255,0) 70%);
  }
  .corner-ornament.tl { left: 22px; top: 22px; }
  .corner-ornament.tr { right: 22px; top: 22px; }
  .corner-ornament.bl { left: 22px; bottom: 22px; }
  .corner-ornament.br { right: 22px; bottom: 22px; }

  .sign-brand {
    position: absolute; left: 0; right: 0; top: 54px;
    display: flex; justify-content: center; align-items: center; gap: 12px;
    font-family: "Kaushan Script", cursive;
    font-size: 48px; line-height: 1; color: var(--white);
  }
  .brand-dot {
    width: 24px; height: 24px; border-radius: 50%; background: var(--glow);
    flex: none;
  }

  .egg-panel { position: absolute; left: 154px; top: 154px; width: 520px; height: 376px; }
  .egg-panel > svg { position: absolute; inset: 0; }
  .panel-tagline {
    font-family: "Kaushan Script", cursive; font-size: 40px; fill: var(--ink);
  }
  .panel-organic {
    position: absolute; left: 0; right: 0; top: 96px; text-align: center;
    font-family: "Libre Baskerville", Georgia, serif; font-weight: 700;
    font-size: 27px; line-height: 1; color: var(--ink);
  }
  .panel-range {
    position: absolute; left: 0; right: 0; top: 126px; text-align: center;
    font-family: "Libre Baskerville", Georgia, serif; font-weight: 700;
    font-size: 17px; line-height: 1; color: var(--ink);
  }
  .panel-eggs {
    position: absolute; left: 0; right: 0; top: 136px; text-align: center;
    font-family: "Anton", Impact, sans-serif; font-size: 126px;
    line-height: 1; color: var(--ink);
  }
  .panel-eggs span { display: inline-block; transform: scaleX(.8); }
  .hen {
    position: absolute; top: 156px; width: 88px; height: 96px;
    background: var(--ink); border-radius: 45% 55% 35% 40%;
  }
  .hen.left { left: 16px; }
  .hen.right { right: 16px; }
  .sale-bar {
    position: absolute; left: 16px; top: 256px; width: 496px; height: 56px;
    background: var(--white); border: 3px solid var(--bar-edge); border-radius: 16px;
  }
  .sale-bar .spark { position: absolute; top: 8px; width: 36px; height: 36px; }
  .sale-bar .spark.left { left: 42px; }
  .sale-bar .spark.right { right: 42px; }
  .sale-bar .label {
    position: absolute; left: 0; right: 0; top: 0; height: 50px;
    display: flex; align-items: center; justify-content: center;
    font-family: "Libre Baskerville", Georgia, serif; font-weight: 700;
    font-size: 46px; line-height: 1; color: var(--ink); letter-spacing: 1px;
  }
  .panel-flourish {
    position: absolute; left: 172px; top: 318px; width: 188px; height: 38px;
    background: radial-gradient(ellipse at center, rgba(20,30,30,.45), rgba(20,30,30,0) 70%);
  }

  .sign-phone {
    position: absolute; left: 0; right: 0; top: 536px; text-align: center;
    font-family: "Libre Baskerville", Georgia, serif; font-weight: 700;
    font-size: 42px; line-height: 1.2; color: var(--white);
  }
  .sign-phone::before, .sign-phone::after {
    content: ""; display: inline-block; width: 36px; height: 2px;
    background: var(--white); vertical-align: middle; margin: 0 22px;
  }

  .brand-logo {
    position: absolute; left: 0; right: 0; top: 960px;
    display: flex; justify-content: center; align-items: center; gap: 22px;
    font-family: "Kaushan Script", cursive; font-size: 88px; line-height: 1;
    color: var(--ink);
  }
  .brand-logo .brand-dot { width: 46px; height: 46px; }
</style>
</head>
<body>
  <section class="presentation-board">
    <div class="sign-shadow"></div>
    <div class="sign">
      <div class="sign-wood" role="img" aria-label="Weathered dark brown wooden plank background"></div>
      <div class="corner-ornament tl" role="img" aria-label="White scroll ornament, top left corner"></div>
      <div class="corner-ornament tr" role="img" aria-label="White scroll ornament, top right corner"></div>
      <div class="corner-ornament bl" role="img" aria-label="White scroll ornament, bottom left corner"></div>
      <div class="corner-ornament br" role="img" aria-label="White scroll ornament, bottom right corner"></div>

      <div class="sign-brand"><span class="brand-dot"></span><span>Bramble Nook Acres</span></div>

      <div class="egg-panel">
        <svg viewBox="0 0 520 376" width="520" height="376">
          <defs>
            <radialGradient id="panelGlow" cx="50%" cy="55%" r="60%">
              <stop offset="0" stop-color="#ffffff"/>
              <stop offset=".45" stop-color="#bfe6ef"/>
              <stop offset="1" stop-color="#5ea7b2"/>
            </radialGradient>
            <path id="taglineArc" d="M30 160 Q260 -60 495 175" fill="none"/>
          </defs>
          <ellipse cx="260" cy="188" rx="259" ry="187" fill="#e2cfc6" opacity=".85"/>
          <ellipse cx="260" cy="188" rx="251" ry="179" fill="url(#panelGlow)"/>
          <text class="panel-tagline" text-anchor="middle"><textPath href="#taglineArc" startOffset="50%">Fresh From The Farm</textPath></text>
        </svg>
        <div class="panel-organic">ORGANIC</div>
        <div class="panel-range">FREE RANGE</div>
        <div class="panel-eggs"><span>EGGS</span></div>
        <div class="hen left" role="img" aria-label="Black hen silhouette standing on grass"></div>
        <div class="hen right" role="img" aria-label="Black hen silhouette standing on grass"></div>
        <div class="sale-bar">
          <svg class="spark left" viewBox="0 0 36 36"><g stroke="#111" stroke-width="2"><line x1="18" y1="1" x2="18" y2="35"/><line x1="1" y1="18" x2="35" y2="18"/><line x1="6" y1="6" x2="30" y2="30"/><line x1="30" y1="6" x2="6" y2="30"/></g></svg>
          <span class="label">FOR SALE</span>
          <svg class="spark right" viewBox="0 0 36 36"><g stroke="#111" stroke-width="2"><line x1="18" y1="1" x2="18" y2="35"/><line x1="1" y1="18" x2="35" y2="18"/><line x1="6" y1="6" x2="30" y2="30"/><line x1="30" y1="6" x2="6" y2="30"/></g></svg>
        </div>
        <div class="panel-flourish" role="img" aria-label="Dark scroll flourish ornament"></div>
      </div>

      <div class="sign-phone">Call:(555)014-2276</div>
    </div>
  </section>

  <div class="brand-logo"><span class="brand-dot"></span><span>Bramble Nook Acres</span></div>
</body>
</html>
```